VELTA CORE

I am in this industry for last 15 years we have done lots of commercial site like we work with BRAVEN costruction, lumo properties, TWD, penwick construction.
We do all domestic and commercial wall and floor tiling, swimming pools, spas, paving, marbles blue stones and muchmore.

Specializing in the wall and floor Tiling, Waterproofing and floor preparations

Industry/Entity Type

Industry

Number of Pages Required

1 page

Font styles to use
Serif
Decorative

Colors

Designer to choose colors to be used in the design.

Requirements
Must have
• domestic and commercial indoor tiling, bathroom tiling and paving pictures
Nice to have
• beautiful bathroom pictures with tile

```html
<!DOCTYPE html>
<html lang="en">
<head>
<meta charset="utf-8">
<title>VELTA CORE — Wall &amp; Floor Tiling</title>
<link href="https://fonts.googleapis.com/css2?family=Playfair+Display:wght@400;700&family=Open+Sans:wght@400;600&display=swap" rel="stylesheet">
<style>
:root{
  --green:#94c83d;
  --green-dark:#7fb12e;
  --ink:#222;
  --text:#666;
  --muted:#999;
  --line:#e6e6e6;
  --stats-bg:#efefef;
  --footer:#434b57;
  --footer-line:#56606d;
  --footer-bottom:#3a414b;
  --white:#fff;
  --serif:'Playfair Display', Georgia, serif;
  --sans:'Open Sans', Arial, sans-serif;
}
*{box-sizing:border-box;margin:0;padding:0}
html,body{width:1200px;height:3220px;overflow:hidden}
body{position:relative;background:var(--white);font-family:var(--sans);color:var(--text)}
section,header,footer{position:absolute;left:0;width:1200px}
.abs{position:absolute}
.section-title{position:absolute;left:0;width:1200px;text-align:center;font-family:var(--serif);font-size:27px;color:var(--ink)}
.section-title::after{content:"";display:block;width:28px;height:2px;background:#cfcfcf;margin:12px auto 0}

/* hero */
.hero{top:0;height:575px}
.hero-photo{position:absolute;inset:0;background:linear-gradient(100deg,#8c8279 0%,#a89f94 30%,#7d7468 48%,#a38a5c 68%,#c9a25f 82%,#e2d7c6 100%)}
.hero-shade{position:absolute;inset:0;background:rgba(0,0,0,.12)}
.logo{position:absolute;left:88px;top:36px;font-family:var(--sans);font-weight:600;font-size:18px;color:var(--white);letter-spacing:.5px}
.nav{position:absolute;top:38px;left:0;width:1200px}
.nav a{position:absolute;font-size:13px;color:var(--white);text-decoration:none;white-space:nowrap}
.nav .active::before{content:"";position:absolute;left:-4px;right:-4px;top:-38px;height:4px;background:var(--green)}
.hero-title{position:absolute;top:232px;left:0;width:1200px;text-align:center;font-family:var(--serif);font-size:36px;line-height:48px;color:var(--white)}
.btn-green{position:absolute;left:543px;top:350px;width:116px;height:39px;background:var(--green);color:var(--white);font-size:12px;line-height:39px;text-align:center}
.slider-dots span{position:absolute;left:1151px;width:9px;height:9px;border-radius:50%;background:rgba(255,255,255,.7)}
.slider-dots .on{background:var(--green)}

/* about */
.about{top:575px;height:387px}
.about p{position:absolute;left:205px;top:159px;width:790px;text-align:center;font-size:12.5px;line-height:23px;color:var(--text)}
.btn-outline{position:absolute;left:533px;top:251px;width:134px;height:44px;border:2px solid var(--green);color:var(--green);font-size:11px;line-height:40px;text-align:center}

/* services */
.services{top:962px;height:438px;background:linear-gradient(180deg,#9acd43,#8fc33a)}
.services .section-title{color:var(--white);top:72px}
.services .section-title::after{background:rgba(255,255,255,.8)}
.service{position:absolute;top:177px;width:220px;text-align:center}
.service .icon{width:104px;height:104px;border-radius:50%;background:var(--white);margin:0 auto;display:flex;align-items:center;justify-content:center}
.service .label{margin-top:28px;font-family:var(--serif);font-size:18px;color:var(--white)}

/* work */
.work{top:1400px;height:543px}
.card{position:absolute;top:152px;width:324px;height:340px}
.card .photo{height:221px}
.card .name{text-align:center;font-family:var(--serif);font-size:18px;color:#333;margin-top:26px}
.card .rule{height:1px;background:var(--line);margin:14px 24px 0}
.card .more{text-align:center;font-size:11px;color:var(--muted);margin-top:18px;letter-spacing:.3px}
.card.featured{box-shadow:0 12px 30px rgba(0,0,0,.12)}
.card.featured .more{color:var(--green)}

/* stats */
.stats{top:1943px;height:247px;background:var(--stats-bg)}
.stat{position:absolute;top:55px;width:240px;text-align:center}
.stat .num{position:relative;font-family:var(--sans);font-weight:600;font-size:62px;line-height:70px;color:#3c3c3c;letter-spacing:-2px}
.stat .num::before{content:"";position:absolute;left:86px;top:6px;width:2px;height:64px;background:#cfcfcf;transform:rotate(-35deg)}
.stat .label{margin-top:12px;font-family:var(--serif);font-size:18px;color:#444}

/* testimonials */
.testimonials{top:2190px;height:468px}
.stars{position:absolute;top:148px;left:0;width:1200px;text-align:center}
.quote{position:absolute;left:205px;top:188px;width:790px;text-align:center;font-size:12.5px;line-height:23px}
.client{position:absolute;top:248px;left:0;width:1200px;text-align:center;font-size:13px;font-weight:600;color:#222}
.avatar{position:absolute;top:292px;width:52px;height:52px;border-radius:50%}
.t-dots span{position:absolute;top:378px;width:6px;height:6px;border-radius:50%;background:#cfe4a8}
.t-dots .on{background:var(--green)}

/* footer */
.footer{top:2658px;height:562px;background:var(--footer);color:#d5d9de}
.newsletter-title{position:absolute;left:88px;top:56px;font-family:var(--serif);font-size:19px;color:var(--white)}
.news-input{position:absolute;left:558px;top:47px;width:430px;height:46px;background:var(--white);font-size:11px;color:var(--muted);line-height:46px;padding-left:18px}
.news-btn{position:absolute;left:988px;top:47px;width:122px;height:46px;background:var(--green);color:var(--white);font-size:12px;line-height:46px;text-align:center}
.divider{position:absolute;left:88px;top:140px;width:1024px;height:1px;background:var(--footer-line)}
.col-divider{position:absolute;left:510px;top:196px;width:1px;height:250px;background:var(--footer-line)}
.f-title{position:absolute;top:198px;font-family:var(--serif);font-size:17px;color:var(--white)}
.info{position:absolute;left:88px;font-size:12px;line-height:23px;color:#d5d9de;display:flex;gap:10px}
.info svg{flex:none;margin-top:5px}
.field-label{position:absolute;font-size:13px;color:var(--white)}
.field{position:absolute;font-size:11px;color:#c8cdd3;padding-bottom:12px;border-bottom:1px solid var(--footer-line)}
.send{position:absolute;left:623px;top:406px;width:78px;height:41px;background:var(--white);color:#333;font-size:11px;font-weight:600;line-height:41px;text-align:center}
.bottom-bar{position:absolute;left:0;top:511px;width:1200px;height:51px;background:var(--footer-bottom);text-align:center;font-size:11px;line-height:51px;color:#d5d9de}
.to-top{position:absolute;left:1133px;top:491px;width:40px;height:40px;border-radius:50%;background:var(--white);display:flex;align-items:center;justify-content:center}
</style>
</head>
<body>

<header class="hero">
  <div class="hero-photo" role="img" aria-label="Photo of a modern bathroom with glass shower doors and a marble tiled vanity"></div>
  <div class="hero-shade"></div>
  <div class="logo">VELTA CORE</div>
  <nav class="nav">
    <a class="active" style="left:641px">Home</a>
    <a style="left:706px">About us</a>
    <a style="left:787px">Services</a>
    <a style="left:866px">Our Work</a>
    <a style="left:948px">Our Partners</a>
    <a style="left:1047px">Contact us</a>
  </nav>
  <h1 class="hero-title">Domestic &amp; Commercial<br>Wall &amp; Floor Tiling</h1>
  <div class="btn-green">Learn More</div>
  <div class="slider-dots">
    <span style="top:268px"></span>
    <span class="on" style="top:289px"></span>
    <span style="top:310px"></span>
  </div>
</header>

<section class="about">
  <h2 class="section-title" style="top:87px">About Us</h2>
  <p>This is Photoshop's version of Lorem Ipsum. Proin gravida nibh vel velit auctor aliquet. Aenean sollicitudin, lorem quis bibendum auctor, nisi elit consequat ipsum, nec sagittis sem nibh id elit. Duis sed odio sit amet nibh vulputate cursus a sit amet mauris. Morbi accumsan ipsum velit. Nam nec tellus a odio tincidunt auctor a ornare odio...</p>
  <div class="btn-outline">READ MORE</div>
</section>

<section class="services">
  <h2 class="section-title">Our Services</h2>
  <div class="service" style="left:32px">
    <div class="icon"><svg width="54" height="54" viewBox="0 0 54 54" fill="none" stroke="#222" stroke-width="2"><path d="M27 8 46 27 27 46 8 27Z"/><path d="M17.5 17.5 36.5 36.5M36.5 17.5 17.5 36.5"/></svg></div>
    <div class="label">Floor Tiling</div>
  </div>
  <div class="service" style="left:258px">
    <div class="icon"><svg width="54" height="54" viewBox="0 0 54 54" fill="none" stroke="#222" stroke-width="2"><path d="M20 36V14a5 5 0 0 1 10 0M32 36V14a5 5 0 0 1 10 0M20 22h12M20 30h12"/><path d="M8 40q4-3 8 0t8 0 8 0 8 0 8 0M8 46q4-3 8 0t8 0 8 0 8 0 8 0"/></svg></div>
    <div class="label">Swimming Pools</div>
  </div>
  <div class="service" style="left:490px">
    <div class="icon"><svg width="54" height="54" viewBox="0 0 54 54" fill="none" stroke="#222" stroke-width="2"><path d="M27 12c6 6 6 16 0 24-6-8-6-18 0-24Z"/><path d="M27 36c-6-2-12-8-13-16 6 0 11 3 13 8M27 36c6-2 12-8 13-16-6 0-11 3-13 8"/><path d="M27 36c-8 2-15-1-18-6M27 36c8 2 15-1 18-6"/></svg></div>
    <div class="label">Spas</div>
  </div>
  <div class="service" style="left:708px">
    <div class="icon"><svg width="56" height="54" viewBox="0 0 56 54" fill="none" stroke="#222" stroke-width="2"><path d="M14 16h28l8 22H6Z"/><path d="M10 27h36M21 16l-4 22M28 16v22M35 16l4 22M17 16l-3 11M24 27l-2 11M32 27l2 11M39 16l3 11"/></svg></div>
    <div class="label">Paving</div>
  </div>
  <div class="service" style="left:933px">
    <div class="icon"><svg width="54" height="54" viewBox="0 0 54 54" fill="none" stroke="#222" stroke-width="2"><ellipse cx="27" cy="16" rx="8" ry="4"/><ellipse cx="27" cy="27" rx="12" ry="5"/><ellipse cx="27" cy="39" rx="16" ry="6"/></svg></div>
    <div class="label">Marbles blue stones</div>
  </div>
</section>

<section class="work">
  <h2 class="section-title" style="top:75px">Our Work</h2>
  <div class="card" style="left:88px">
    <div class="photo" role="img" aria-label="Photo of a living room with tiled floor" style="background:linear-gradient(135deg,#6a5646,#b9a58a 55%,#e4dccd)"></div>
    <div class="name">Indoor Tiling</div><div class="rule"></div>
    <div class="more">+ VIEW DETAILS</div>
  </div>
  <div class="card featured" style="left:438px">
    <div class="photo" role="img" aria-label="Photo of a white tiled commercial bathroom wall" style="background:linear-gradient(180deg,#e4e6e6,#c9cdcf 60%,#8c9094)"></div>
    <div class="name">Bathroom Tiling</div><div class="rule"></div>
    <div class="more">+ VIEW DETAILS</div>
  </div>
  <div class="card" style="left:788px">
    <div class="photo" role="img" aria-label="Photo of a brick paved waterfront promenade" style="background:linear-gradient(180deg,#b8c4cc 0%,#9fa9ae 35%,#5f7478 55%,#9a5a48 80%,#7c463a)"></div>
    <div class="name">Paving Pictures</div><div class="rule"></div>
    <div class="more">+ VIEW DETAILS</div>
  </div>
</section>

<section class="stats">
  <div class="stat" style="left:52px"><div class="num">25</div><div class="label">Satisfied Customer</div></div>
  <div class="stat" style="left:318px"><div class="num">37</div><div class="label">World Wide Client</div></div>
  <div class="stat" style="left:584px"><div class="num">30</div><div class="label">Staffs Employees</div></div>
  <div class="stat" style="left:885px"><div class="num">85</div><div class="label">Comleted Projects</div></div>
</section>

<section class="testimonials">
  <h2 class="section-title" style="top:83px">Client's Testimonials</h2>
  <div class="stars">
    <svg width="122" height="22" viewBox="0 0 122 22" fill="#f0a22e">
      <path d="M11 1l3 7 7 .5-5.5 4.5 2 7L11 16l-6.5 4 2-7L1 8.5 8 8Z"/>
      <path transform="translate(25 0)" d="M11 1l3 7 7 .5-5.5 4.5 2 7L11 16l-6.5 4 2-7L1 8.5 8 8Z"/>
      <path transform="translate(50 0)" d="M11 1l3 7 7 .5-5.5 4.5 2 7L11 16l-6.5 4 2-7L1 8.5 8 8Z"/>
      <path transform="translate(75 0)" d="M11 1l3 7 7 .5-5.5 4.5 2 7L11 16l-6.5 4 2-7L1 8.5 8 8Z"/>
      <path transform="translate(100 0)" d="M11 1l3 7 7 .5-5.5 4.5 2 7L11 16l-6.5 4 2-7L1 8.5 8 8Z" opacity=".55"/>
    </svg>
  </div>
  <p class="quote">Lorem ipsum dolor sit amet consectetuer adipiscing elit aenean commodo ligula eget dolor aenean massa cum sociis natoque penatibus et magnis dis parturient montes nascetur ridiculus mus donec quam felis ultricies nec.</p>
  <div class="client">MARISSA HOLLOWAY</div>
  <div class="avatar" role="img" aria-label="Client portrait" style="left:414px;background:#e8e4e0;box-shadow:0 4px 10px rgba(0,0,0,.15)"></div>
  <div class="avatar" role="img" aria-label="Client portrait" style="left:494px;background:#3b3633"></div>
  <div class="avatar" role="img" aria-label="Client portrait" style="left:574px;background:#d9b08c"></div>
  <div class="avatar" role="img" aria-label="Client portrait" style="left:654px;background:#4f6b78"></div>
  <div class="avatar" role="img" aria-label="Client portrait" style="left:734px;background:#c25a8a"></div>
  <div class="t-dots">
    <span class="on" style="left:584px"></span><span style="left:597px"></span><span style="left:610px"></span>
  </div>
</section>

<footer class="footer">
  <div class="newsletter-title">Subscribe To Our Email Newsletter</div>
  <div class="news-input">Enter email address...</div>
  <div class="news-btn">Subscribe</div>
  <div class="divider"></div>

  <div class="f-title" style="left:88px">Contact information</div>
  <div class="info" style="top:238px">
    <svg width="11" height="13" viewBox="0 0 11 13"><path d="M5.5 0A5 5 0 0 0 .5 5c0 3.5 5 8 5 8s5-4.5 5-8a5 5 0 0 0-5-5Zm0 7a2 2 0 1 1 0-4 2 2 0 0 1 0 4Z" fill="var(--green)"/></svg>
    <span>Address:Some address line goes here. City name,<br>Country name here.</span>
  </div>
  <div class="info" style="top:292px">
    <svg width="11" height="12" viewBox="0 0 11 12"><path d="M2 0l2.5 3-1.2 1.6a7 7 0 0 0 3.3 3.3L8 6.7l3 2.5L9.5 11.5C5 11.5-.5 6 .5 1.5Z" fill="var(--green)"/></svg>
    <span>Phone: 123 456 7890</span>
  </div>
  <div class="info" style="top:326px">
    <svg width="12" height="10" viewBox="0 0 12 10"><rect width="12" height="9" rx="1" fill="var(--green)"/><path d="M0 1l6 4 6-4" stroke="#434b57" fill="none"/></svg>
    <span>Email: info@example.com</span>
  </div>
  <div class="info" style="top:363px">
    <svg width="12" height="11" viewBox="0 0 12 11"><rect x="2" width="8" height="4" fill="var(--green)"/><rect y="4" width="12" height="5" rx="1" fill="var(--green)"/><rect x="2" y="7" width="8" height="4" fill="var(--green)"/></svg>
    <span>Fax: 123 546 7890</span>
  </div>

  <div class="col-divider"></div>
  <div class="f-title" style="left:623px">Contact now</div>
  <div class="field-label" style="left:623px;top:246px">Name:</div>
  <div class="field" style="left:623px;top:272px;width:235px">Enter your name...</div>
  <div class="field-label" style="left:875px;top:246px">Email:</div>
  <div class="field" style="left:875px;top:272px;width:235px">Enter your email...</div>
  <div class="field-label" style="left:623px;top:316px">Message:</div>
  <div class="field" style="left:623px;top:342px;width:487px;padding-bottom:24px">Enter your message...</div>
  <div class="send">SEND</div>

  <div class="bottom-bar">© 2017 All Rights Reserved</div>
  <div class="to-top"><svg width="12" height="8" viewBox="0 0 12 8"><path d="M1 7l5-5 5 5" stroke="#333" stroke-width="2" fill="none"/></svg></div>
</footer>

</body>
</html>
```